New website for actress www.marlene-vogtberg.de

My website is a little old and needs a new look.
I am a german actress who is in the TV and Theaterbusiness.
my chirpnet account is called MarVogtberg
this design will be set up as wordpress site and needs to be optimized for mobile,
so please provide mobile screen views too.
the content will not change much from the excisting site but I would like to have a news section with Videos and press Releases
I would also like my chirpnet feed to be displayed on my landing page.
I am looking forward to your ideas
best regards
marlene

Target Market(s)

press and fans

Industry/Entity Type

Tv

Font styles to use
Serif
Sans Serif

Colors

Designer to choose colors to be used in the design.

Requirements
Must have
• see above

```html
<!DOCTYPE html>
<html lang="de">
<head>
<meta charset="utf-8">
<title>Marlene Vogtberg</title>
<link rel="stylesheet" href="https://fonts.googleapis.com/css2?family=Noto+Serif:wght@400;700&family=Open+Sans:wght@400;600;700&display=swap">
<style>
:root{
  --red:#c8313a;
  --dark:#1f1f1f;
  --ink:#333;
  --muted:#888;
  --line:#e2e2e2;
  --panel:#f4f4f4;
  --white:#fff;
  --chirp:#4aa8de;
  --folk:#3b5a98;
  --plus:#d34836;
  --vid:#cc2b22;
  --pin:#bd2129;
  --snap:#5b86a8;
}
*{box-sizing:border-box;margin:0;padding:0}
html,body{width:1200px;height:2176px;overflow:hidden}
body{position:relative;background:var(--white);font-family:"Open Sans",Arial,sans-serif;color:var(--ink);font-size:13px}
.abs{position:absolute}
.serif{font-family:"Noto Serif",Georgia,serif}
.photo{position:absolute;background:linear-gradient(160deg,#9a9a9a,#5e5e5e)}
.photo.warm{background:linear-gradient(160deg,#d8b28a,#8a6a52)}
.photo.mono{background:linear-gradient(160deg,#c9c9c9,#6f6f6f)}
.photo.dark{background:linear-gradient(160deg,#3a3a3a,#101010)}

.topbar{left:0;top:0;width:1200px;height:28px;background:var(--dark);color:#bbb;font-size:11px}
.topbar .date{left:56px;top:7px}
.topbar .contact{left:230px;top:7px;color:#ddd}
.topbar .search{left:760px;top:5px;width:200px;height:18px;background:#333;color:#888;padding:2px 8px;font-size:10px}
.topbar .dots{left:1040px;top:7px;display:flex;gap:6px}
.topbar .dots span{width:14px;height:14px;border-radius:50%;display:block}

.logo{left:56px;top:42px;font-size:38px;color:var(--red);font-weight:400}

.nav{left:56px;top:100px;width:1088px;height:34px;border-top:1px solid var(--line);border-bottom:1px solid var(--line);display:flex;font-size:12px;color:#555}
.nav a{display:block;padding:9px 20px;text-decoration:none;color:inherit;border-right:1px solid var(--line)}
.nav a.active{color:var(--red)}

.ticker{left:56px;top:148px;width:1088px;height:20px;font-size:10px;color:#666}
.ticker .label{position:absolute;left:0;top:0;background:var(--red);color:#fff;font-weight:700;padding:3px 8px;height:20px}
.ticker .text{position:absolute;left:110px;top:3px}
.arrows{position:absolute;display:flex;gap:2px}
.arrows span{width:18px;height:18px;background:#ddd;color:#555;font-size:11px;text-align:center;line-height:18px;display:block}

.hero{left:56px;top:176px;width:1088px;height:584px}
.hero .caption{position:absolute;left:0;bottom:0;width:100%;height:130px;background:rgba(0,0,0,.6);padding:18px 26px;color:#fff}
.tag{display:inline-block;background:var(--red);color:#fff;font-size:10px;padding:3px 8px}
.hero .date{font-size:11px;color:#ddd;margin-left:10px}
.hero h1{font-size:28px;font-weight:400;margin-top:10px}
.hero .by{font-size:10px;color:#bbb;margin-top:6px;text-transform:uppercase}

.sectitle{font-size:14px;text-transform:uppercase;color:var(--ink);border-bottom:2px solid #ccc;padding-bottom:6px}
.newsrow{left:56px;top:820px;width:872px;display:flex;gap:12px}
.newsitem{position:relative;width:209px;height:140px}
.newsitem .cap{position:absolute;left:0;bottom:0;width:100%;background:rgba(0,0,0,.6);color:#fff;font-size:10px;padding:5px 8px;line-height:1.3}

.tabs{left:944px;top:808px;width:200px}
.tabs .heads{display:flex;font-size:11px;border-bottom:1px solid var(--line)}
.tabs .heads span{flex:1;text-align:center;padding:6px 0}
.tabs .heads .on{border-bottom:2px solid var(--red);color:var(--red)}
.popitem{display:flex;gap:8px;padding:10px 0;border-bottom:1px solid var(--line);font-size:10px;line-height:1.35}
.popitem .th{width:46px;height:36px;flex:none;position:relative}
.stars{color:#e0a526;font-size:11px}

.video-main{left:56px;top:1108px;width:324px;height:230px}
.play{position:absolute;left:50%;top:50%;transform:translate(-50%,-50%)}
.video-text{left:400px;top:1104px;width:480px}
.video-text h2{font-size:22px;font-weight:400;line-height:1.25}
.video-text .by{font-size:10px;color:var(--muted);margin:6px 0 14px}
.video-text p{font-size:11px;line-height:1.6;color:#555;margin-bottom:10px}
.btn{display:inline-block;background:var(--red);color:#fff;font-size:10px;font-weight:700;padding:7px 16px;text-transform:uppercase}
.smallvid{position:absolute;width:420px;height:84px;display:flex;gap:14px}
.smallvid .th{width:118px;height:84px;flex:none;position:relative}
.smallvid p{font-size:11px;line-height:1.5;color:#555}
.smallvid .d{font-size:9px;color:var(--muted);margin-top:4px}

.follow{left:944px;top:1212px;width:200px}
.srow{display:flex;align-items:center;gap:10px;padding:7px 0;border-bottom:1px solid var(--line);font-size:10px;color:#555}
.srow i{width:22px;height:22px;display:block;flex:none}
.feed{left:944px;top:1500px;width:200px}
.followbtn{display:inline-block;border:1px solid #ccc;border-radius:3px;background:#f2f2f2;font-size:10px;font-weight:700;padding:4px 10px;margin:12px 0}
.tweet{font-size:10px;line-height:1.5;color:#555;margin-bottom:12px}
.tweet b{color:var(--chirp);font-weight:400}
.tweet .ago{display:block;color:var(--muted);font-size:9px}

.albums{left:56px;top:1768px;width:872px;display:flex;gap:12px}
.album{position:relative;width:283px;height:190px}
.album .cap{position:absolute;left:0;bottom:0;width:100%;background:rgba(0,0,0,.6);color:#fff;font-size:10px;padding:6px 8px;line-height:1.3}

.footer{left:0;top:2146px;width:1200px;height:30px;background:var(--dark)}
</style>
</head>
<body>

<header>
  <div class="abs topbar">
    <span class="abs date">Wednesday 5 February 2014</span>
    <span class="abs contact">Contact Me</span>
    <span class="abs search">Search ...</span>
    <div class="abs dots">
      <span style="background:var(--chirp)"></span>
      <span style="background:var(--folk)"></span>
      <span style="background:var(--plus)"></span>
      <span style="background:var(--vid)"></span>
      <span style="background:#e08a2c"></span>
    </div>
  </div>

  <div class="abs logo serif">Marlene Vogtberg</div>

  <nav class="abs nav">
    <a class="active">Home</a><a>Biographie</a><a>Interviews</a><a>Theaterkritiken</a><a>Pressefotos</a><a>Kritiken</a><a>Autogramme</a><a>Charity</a><a>Kontakt</a>
  </nav>

  <div class="abs ticker">
    <span class="label">BREAKING NEWS</span>
    <span class="text">Lorem ipsum dolor sit amet, consectetur adipiscing elit, sed do eiusmod tempor</span>
    <div class="arrows" style="right:0;top:1px"><span>&lsaquo;</span><span>&rsaquo;</span></div>
  </div>
</header>

<main>
  <section class="abs hero">
    <div class="photo mono" style="inset:0" role="img" aria-label="Black and white portrait photograph of the actress"></div>
    <div class="arrows" style="right:10px;top:270px"><span>&lsaquo;</span><span>&rsaquo;</span></div>
    <div class="caption">
      <span class="tag">Interviews</span><span class="date">January 7th, 2014</span>
      <h1 class="serif">Quis Dignissim Mauris Dolor Eget Mi: Donec At Mauris Enim.</h1>
      <div class="by">By Marlene Vogtberg</div>
    </div>
  </section>

  <div class="abs" style="left:56px;top:782px;width:872px">
    <div class="sectitle">Latest News</div>
    <div class="arrows" style="right:0;top:0"><span>&lsaquo;</span><span>&rsaquo;</span></div>
  </div>
  <div class="abs newsrow">
    <div class="newsitem"><div class="photo warm" style="inset:0" role="img" aria-label="Press photo of the actress smiling"></div><div class="cap">Quis Dignissim Mauris Dolor Eget Mi: Donec At Mauris</div></div>
    <div class="newsitem"><div class="photo mono" style="inset:0" role="img" aria-label="Black and white press photo of the actress"></div><div class="cap">Quis Dignissim Mauris Dolor Eget Mi: Donec At Mauris</div></div>
    <div class="newsitem"><div class="photo" style="inset:0;background:linear-gradient(160deg,#e8c7c0,#a04a5a)" role="img" aria-label="Magazine cover featuring the actress"></div><div class="cap">Mauris Dolor Eget Mi: Donec At Mauris Enim</div></div>
    <div class="newsitem"><div class="photo warm" style="inset:0" role="img" aria-label="Event photo of the actress"></div><div class="cap">Donec At Mauris Enim Quis Dignissim</div></div>
  </div>

  <div class="abs" style="left:56px;top:1070px;width:872px"><div class="sectitle">Latest Videos</div></div>
  <div class="abs video-main">
    <div class="photo" style="inset:0;background:linear-gradient(160deg,#cfd6dc,#7d8b96)" role="img" aria-label="Video still of the actress in a TV role"></div>
    <svg class="play" width="44" height="44" viewBox="0 0 44 44"><circle cx="22" cy="22" r="21" fill="rgba(0,0,0,.5)"/><path d="M17 13 L31 22 L17 31 Z" fill="#fff"/></svg>
  </div>
  <div class="abs video-text">
    <h2 class="serif">Quis Dignissim Mauris Dolor Eget Mi: Donec Mauris</h2>
    <div class="by">By Marlene Vogtberg &nbsp; Leave a comment</div>
    <p>Lorem ipsum dolor sit amet, consectetur adipiscing elit, sed do eiusmod tempor incididunt ut labore et dolore magna aliqua enim ad minim.</p>
    <p>Lorem ipsum dolor sit amet, consectetur adipiscing elit, sed do eiusmod tempor incididunt ut labore et dolore magna aliqua.</p>
    <span class="btn">Read more</span>
  </div>

  <div class="smallvid" style="left:56px;top:1360px">
    <div class="th photo dark" role="img" aria-label="Video still"><svg class="play" width="22" height="22" viewBox="0 0 22 22"><path d="M6 3 L19 11 L6 19 Z" fill="#fff"/></svg></div>
    <div><p>Lorem ipsum dolor sit amet, adipiscing elit sed do tempor incididunt ut labore.</p><div class="d">January 7th, 2014</div></div>
  </div>
  <div class="smallvid" style="left:500px;top:1360px">
    <div class="th photo dark" role="img" aria-label="Video still"><svg class="play" width="22" height="22" viewBox="0 0 22 22"><path d="M6 3 L19 11 L6 19 Z" fill="#fff"/></svg></div>
    <div><p>Lorem ipsum dolor sit amet, adipiscing elit sed do tempor incididunt ut labore.</p><div class="d">January 7th, 2014</div></div>
  </div>
  <div class="smallvid" style="left:56px;top:1464px">
    <div class="th photo dark" role="img" aria-label="Video still"><svg class="play" width="22" height="22" viewBox="0 0 22 22"><path d="M6 3 L19 11 L6 19 Z" fill="#fff"/></svg></div>
    <div><p>Lorem ipsum dolor sit amet, adipiscing elit sed do tempor incididunt ut labore.</p><div class="d">January 7th, 2014</div></div>
  </div>
  <div class="smallvid" style="left:500px;top:1464px">
    <div class="th photo dark" role="img" aria-label="Video still"><svg class="play" width="22" height="22" viewBox="0 0 22 22"><path d="M6 3 L19 11 L6 19 Z" fill="#fff"/></svg></div>
    <div><p>Lorem ipsum dolor sit amet, adipiscing elit sed do tempor incididunt ut labore.</p><div class="d">January 7th, 2014</div></div>
  </div>

  <div class="abs" style="left:56px;top:1732px;width:872px"><div class="sectitle">Photo Albums</div></div>
  <div class="abs albums">
    <div class="album"><div class="photo warm" style="inset:0" role="img" aria-label="Album cover: portrait of the actress"></div><div class="cap">Quis Dignissim Mauris Dolor Eget Mi: Donec At Mauris</div></div>
    <div class="album"><div class="photo mono" style="inset:0" role="img" aria-label="Album cover: black and white photo shoot"></div><div class="cap">Quis Dignissim Mauris Dolor Eget Mi: Donec At Mauris</div></div>
    <div class="album"><div class="photo warm" style="inset:0;background:linear-gradient(160deg,#e6cfa6,#9c7a55)" role="img" aria-label="Album cover: portrait with blonde hair"></div><div class="cap">Quis Dignissim Mauris Dolor Eget Mi: Donec At Mauris</div></div>
  </div>
</main>

<aside>
  <div class="abs tabs">
    <div class="heads"><span class="on">Popular</span><span>Recent</span><span>&#9993;</span></div>
    <div class="popitem"><div class="th photo warm" role="img" aria-label="Thumbnail photo"></div><div>Lorem ipsum dolor sit amet, elit sed do<br><span class="stars">★★★★☆</span></div></div>
    <div class="popitem"><div class="th photo mono" role="img" aria-label="Thumbnail photo"></div><div>Lorem ipsum dolor sit amet, elit sed do<br><span class="stars">★★★☆☆</span></div></div>
    <div class="popitem"><div class="th photo" role="img" aria-label="Thumbnail photo" style="background:linear-gradient(160deg,#8a7aa8,#3e3456)"></div><div>Lorem ipsum dolor sit amet, elit sed do<br><span class="stars">★★★★☆</span></div></div>
    <div class="popitem"><div class="th photo warm" role="img" aria-label="Thumbnail photo"></div><div>Lorem ipsum dolor sit amet, elit sed do<br><span class="stars">★★★★★</span></div></div>
  </div>

  <div class="abs follow">
    <div class="sectitle">Follow Me</div>
    <div class="srow"><i style="background:var(--chirp)"></i>1,254 chirpnet followers</div>
    <div class="srow"><i style="background:var(--folk)"></i>10,456 Pagefolk fans</div>
    <div class="srow"><i style="background:var(--plus)"></i>3,587 Plusring followers</div>
    <div class="srow"><i style="background:var(--pin)"></i>2,245 Pinboardly pins</div>
    <div class="srow"><i style="background:var(--vid)"></i>1,342 Vidstream subscribers</div>
    <div class="srow"><i style="background:var(--snap)"></i>870 Snaplane followers</div>
  </div>

  <div class="abs feed">
    <div class="sectitle">Follow @MarVogtberg</div>
    <span class="followbtn">Follow @MarVogtberg</span>
    <p class="tweet">Drehtag heute in Berlin, danke an das ganze Team für die tolle Zeit! <b>#drehtag #theater</b> <b>chirp.net/a1b2c3</b><span class="ago">2 days ago</span></p>
    <p class="tweet">Neue Pressefotos sind online, schaut gerne vorbei und sagt mir eure Meinung! <b>#pressefotos</b> <b>chirp.net/d4e5f6</b><span class="ago">3 days ago</span></p>
    <p class="tweet">Premiere am Freitag, ich freue mich riesig auf euch alle <b>#premiere</b><span class="ago">5 days ago</span></p>
    <p class="tweet">Check out the new interview on <b>marlene-vogtberg.de</b> <b>#interview #tv</b><span class="ago">6 days ago</span></p>
  </div>
</aside>

<footer class="abs footer"></footer>

</body>
</html>
```